Belford & Company

We are a boutique commercial real estate firm. For our Business card design - sleek, modern, yet high-end/classy. Please see our website: belfordandcompany.example for details.

We currently need 2 business card names and the ability to add/change the business card information -
Name, Title, Address, Office #, Mobile #, Fax, Email and company website.

Industry/Entity Type

Real Estate

Contact Information for Business Card

Business card design - sleek, modern, yet high-end/classy. Please see our website: belfordandcompany.example for details.

Also, we'd like to have our slogan "Patience Earns The Best Results." somewhere in there. We'd like to make some part of it raised or a different texture if possible.
Color #'s:
blue 19 36 128
light gray 222 222 221
dark gray 107 120 128

Also, we'd like to have our slogan "Patience Earns The Best Results." somewhere in there. We'd like to make some part of it raised or a different texture if possible - grey on one side and blue on the other - rounded edges preferred. Maybe either metal/silver/grey raised logo on the back. Thank you!!

Requirements
Must have
• Sleek, modern, clean and classy design

```html
<!DOCTYPE html>
<html lang="en">
<head>
<meta charset="utf-8">
<title>Belford &amp; Company – Business Card</title>
<link href="https://fonts.googleapis.com/css2?family=Old+Standard+TT:wght@400;700&display=swap" rel="stylesheet">
<style>
  :root {
    --navy-deep: #05041a;
    --navy-mid: #141a4a;
    --brand-blue: #2d3a8c;
    --light-gray: #dededd;
    --dark-gray: #6b7880;
    --ink: #2a1a1a;
    --white: #f4f4f4;
    --page: #ffffff;
  }
  * { margin: 0; padding: 0; box-sizing: border-box; }
  html, body { width: 1200px; height: 1200px; overflow: hidden; background: var(--page); }
  body { position: relative; font-family: "Old Standard TT", Georgia, serif; }

  .card { position: absolute; left: 181px; width: 839px; height: 504px; overflow: hidden; }
  .card--front { top: 59px; }
  .card--back { top: 645px; background: var(--light-gray); }

  .photo { position: absolute; }
  .photo--front {
    inset: 0;
    background:
      linear-gradient(135deg, transparent 30%, rgba(60,70,160,0.18) 50%, transparent 70%),
      radial-gradient(ellipse at 50% 20%, var(--navy-mid) 0%, var(--navy-deep) 70%);
  }
  .photo--back {
    left: 0; top: 0; width: 345px; height: 504px;
    background:
      linear-gradient(160deg, transparent 35%, rgba(45,58,140,0.55) 60%, rgba(45,58,140,0.35) 75%, transparent 90%),
      var(--navy-deep);
  }

  .brand-box {
    position: absolute;
    background: var(--brand-blue);
    border: 2px solid var(--dark-gray);
    display: flex; align-items: center; justify-content: center;
  }
  .brand-box--front { left: 272px; top: 155px; width: 295px; height: 164px; }
  .brand-box--back { left: 70px; top: 203px; width: 210px; height: 116px; }
  .brand-name { color: var(--white); font-weight: 700; text-align: center; line-height: 1.1; }
  .brand-box--front .brand-name { font-size: 34px; }
  .brand-box--back .brand-name { font-size: 24px; }

  .slogan {
    position: absolute;
    writing-mode: vertical-rl;
    transform: rotate(180deg);
    color: var(--white);
    font-size: 13px;
    letter-spacing: 4.4px;
    white-space: nowrap;
  }
  .slogan--left { left: 55px; top: 22px; height: 345px; }
  .slogan--right { left: 764px; top: 137px; height: 340px; }

  .rule { position: absolute; width: 1px; }
  .rule--light { background: var(--white); }
  .rule--dark { background: var(--ink); }

  .cross { position: absolute; width: 22px; height: 22px; }

  .contact-name { position: absolute; left: 387px; top: 214px; font-size: 19px; font-weight: 700; letter-spacing: 2px; color: var(--ink); }
  .contact-title { position: absolute; left: 387px; top: 238px; font-size: 14px; font-weight: 700; letter-spacing: 1.5px; color: var(--ink); }

  .contact-row { position: absolute; left: 388px; display: flex; align-items: center; gap: 14px; color: var(--ink); font-size: 13.5px; font-weight: 700; letter-spacing: 1.9px; line-height: 1.3; }
  .contact-row svg { width: 24px; height: 24px; flex: none; }
  .contact-row--address { top: 279px; }
  .contact-row--phone { top: 328px; }
  .contact-row--email { top: 373px; letter-spacing: 1.4px; }
  .contact-row--web { top: 420px; letter-spacing: 1.4px; }
</style>
</head>
<body>

<section class="card card--front">
  <div class="photo photo--front" role="img" aria-label="Upward view of a dark glass tower with blue chevron-shaped facade lines"></div>

  <div class="brand-box brand-box--front">
    <span class="brand-name">Belford<br>&amp; Company</span>
  </div>

  <p class="slogan slogan--left">Patience Earns The Best Results.</p>
  <div class="rule rule--light" style="left:62px; top:373px; height:56px;"></div>
  <svg class="cross" style="left:52px; top:441px;" viewBox="0 0 22 22"><path d="M1 1L21 21M21 1L1 21" stroke="var(--white)" stroke-width="1.5"/></svg>

  <svg class="cross" style="left:762px; top:50px;" viewBox="0 0 22 22"><path d="M1 1L21 21M21 1L1 21" stroke="var(--white)" stroke-width="1.5"/></svg>
  <div class="rule rule--light" style="left:772px; top:76px; height:56px;"></div>
  <p class="slogan slogan--right">Patience Earns The Best Results.</p>
</section>

<section class="card card--back">
  <div class="photo photo--back" role="img" aria-label="Curved blue skyscraper facade rising against a dark sky"></div>

  <div class="brand-box brand-box--back">
    <span class="brand-name">Belford<br>&amp; Company</span>
  </div>

  <svg class="cross" style="left:377px; top:46px;" viewBox="0 0 22 22"><path d="M1 1L21 21M21 1L1 21" stroke="var(--ink)" stroke-width="1.5"/></svg>
  <div class="rule rule--dark" style="left:388px; top:79px; height:96px;"></div>

  <h1 class="contact-name">DIRECTOR NAME</h1>
  <h2 class="contact-title">DESIGNATION</h2>

  <div class="contact-row contact-row--address">
    <svg viewBox="0 0 24 24"><path d="M12 1.5a7.5 7.5 0 0 0-7.5 7.5c0 5.5 7.5 13.5 7.5 13.5s7.5-8 7.5-13.5A7.5 7.5 0 0 0 12 1.5zm0 10.5a3 3 0 1 1 0-6 3 3 0 0 1 0 6z" fill="var(--ink)"/></svg>
    <span>2871 HARBOR BLVD. SUITE #410<br>EASTPORT, FL 32900</span>
  </div>
  <div class="contact-row contact-row--phone">
    <svg viewBox="0 0 24 24"><rect x="6" y="1" width="12" height="22" rx="2" fill="var(--ink)"/><rect x="8" y="4" width="8" height="14" fill="var(--light-gray)"/><circle cx="12" cy="20.5" r="1" fill="var(--light-gray)"/></svg>
    <span>555.013.7280</span>
  </div>
  <div class="contact-row contact-row--email">
    <svg viewBox="0 0 24 24"><rect x="1" y="4" width="22" height="16" rx="1.5" fill="var(--ink)"/><path d="M2 5l10 8 10-8" stroke="var(--light-gray)" stroke-width="1.6" fill="none"/></svg>
    <span>info@belfordandcompany.example</span>
  </div>
  <div class="contact-row contact-row--web">
    <svg viewBox="0 0 24 24" fill="none" stroke="var(--ink)" stroke-width="1.6"><circle cx="12" cy="12" r="10"/><ellipse cx="12" cy="12" rx="4.5" ry="10"/><path d="M2 12h20M4 6.5h16M4 17.5h16"/></svg>
    <span>www.belfordandcompany.example</span>
  </div>

  <div class="rule rule--dark" style="left:766px; top:237px; height:172px;"></div>
  <svg class="cross" style="left:755px; top:419px;" viewBox="0 0 22 22"><path d="M1 1L21 21M21 1L1 21" stroke="var(--ink)" stroke-width="1.5"/></svg>
</section>

</body>
</html>
```